Book cover Back and Front

I need a book cover A5 Size for a book written in Spanish which I will self publish. The title is

LA NOCHE INMENSA DE LOS PUERTOS
MARISOL FUENTEVILLA
The title towards the middle and the name to the right towards the bottom.

The illustration needs to be a hawk with a woman hanging from its beak. I would like something post-modern and exotic.

I also need the spine for a book of 90 pages
In the back cover goes my photo and the bio.

This is a book Book of moden poetry for adults

• The illustration needs to be a hawk with a woman hanging from its beak. I would like something post-modern and exotic.
The file Blurb is what goes on the back cover.
(Please note: not the biography and photo)I don't know how to remove it.

```html
<!DOCTYPE html>
<html lang="es">
<head>
<meta charset="utf-8">
<title>La noche inmensa de los puertos — Cubierta</title>
<link href="https://fonts.googleapis.com/css2?family=Montserrat:wght@500;600;700;800&family=Cormorant+Garamond:wght@500&display=swap" rel="stylesheet">
<style>
  :root{
    --paper:#ffffff;
    --ink:#151515;
    --title-grey:#7b7e84;
    --ghost-grey:#cfcfd1;
    --pink:#c963a6;
    --pink-soft:#d98bbd;
    --violet:#6d3c86;
    --violet-deep:#4b2a60;
    --periwinkle:#7c78b8;
    --cloud:#ececec;
    --label:#8a8a8a;
    --shadow:rgba(0,0,0,.55);
  }
  *{box-sizing:border-box;margin:0;padding:0}
  html,body{width:1200px;height:848px;overflow:hidden;background:var(--paper)}
  body{position:relative;font-family:'Montserrat',sans-serif}

  .cover{position:absolute;width:420px;height:594px;background:var(--paper);overflow:hidden;
    box-shadow:6px 7px 4px var(--shadow);outline:1px solid #d6d6d6}
  .cover--front{left:110px;top:37px}
  .cover--back{left:655px;top:37px}

  .photo{position:absolute}
  .photo--sky{background:linear-gradient(160deg,var(--pink-soft),var(--pink) 60%,#b3568f)}
  .photo--clouds{background:linear-gradient(180deg,#f7f7f7,var(--cloud) 45%,#b9b9b9 80%,#8d8d8d)}
  .photo--facade{background:linear-gradient(180deg,#a9a9a9,#7b7b7b 55%,#5f5f5f)}
  .photo--violet{background:linear-gradient(200deg,#8a5aa3,var(--violet) 50%,var(--violet-deep))}
  .illustration{position:absolute;background:linear-gradient(100deg,#2a2a2a 0%,#5b5b78 30%,var(--periwinkle) 55%,#3a3a44 85%)}

  .title-bar{position:absolute;background:var(--ink);color:#fff;font-weight:600;
    display:flex;align-items:center;letter-spacing:.5px;white-space:nowrap}
  .cover--front .title-bar{left:0;top:238px;width:292px;height:41px;font-size:21px;padding-left:26px}
  .title-joint{position:absolute;left:296px;top:230px;font-size:50px;font-weight:700;
    color:var(--title-grey);line-height:1}
  .title-vertical{position:absolute;writing-mode:vertical-rl;transform:rotate(180deg);
    font-weight:700;line-height:1;white-space:nowrap}
  .cover--front .title-vertical{left:375px;top:4px;height:226px;font-size:30px;color:var(--title-grey);
    text-align:left;letter-spacing:0}
  .author{position:absolute;top:537px;font-size:17px;font-weight:700;letter-spacing:2px;
    white-space:nowrap;line-height:1}
  .author--first{right:186px;color:#fff}
  .author--last{left:241px;color:var(--title-grey)}

  .cover--back .title-vertical{right:2px;top:0;height:594px;font-size:66px;color:var(--ghost-grey);
    text-align:left;letter-spacing:-1px}
  .blurb{position:absolute;background:var(--ink);color:#fff;font-size:10.3px;font-weight:700;
    line-height:1.34;letter-spacing:.35px;text-transform:uppercase;padding:13px 18px 0 13px}
  .blurb--one{left:0;top:125px;width:383px;height:98px}
  .blurb--two{left:35px;top:249px;width:385px;height:96px;text-align:right;padding:13px 14px 0 18px}
  .blurb--three{left:0;top:387px;width:383px;height:97px}

  .spine{position:absolute;left:297px;top:718px;width:595px;height:58px;overflow:hidden;
    background:linear-gradient(90deg,var(--violet-deep) 0%,var(--violet) 28%,#a45a9a 50%,var(--pink) 68%,var(--pink-soft) 100%);
    box-shadow:6px 7px 4px var(--shadow)}
  .spine .title-bar{left:12px;top:9px;width:198px;height:40px;font-size:14.5px;padding-left:14px}
  .spine__title-rest{position:absolute;left:220px;top:8px;font-size:35px;font-weight:700;
    color:rgba(255,255,255,.55);line-height:42px;white-space:nowrap;letter-spacing:-.5px}
  .spine__author{position:absolute;right:13px;top:6px;width:34px;height:46px;background:var(--ink);
    color:#fff;writing-mode:vertical-rl;font-size:6.4px;font-weight:700;letter-spacing:.4px;
    display:flex;align-items:center;justify-content:center;line-height:1.15;text-align:center}

  .label{position:absolute;font-family:'Cormorant Garamond',serif;font-size:17px;font-weight:500;
    letter-spacing:2.6px;color:var(--label)}
</style>
</head>
<body>

<section class="cover cover--front" aria-label="Cubierta frontal">
  <div class="photo photo--sky" role="img" aria-label="Fotografía de cielo con nubes virada a rosa" style="left:0;top:0;width:108px;height:238px"></div>
  <div class="photo photo--clouds" role="img" aria-label="Fotografía de nubes y torre de edificio histórico en blanco y negro" style="left:108px;top:0;width:130px;height:238px"></div>
  <div class="photo photo--violet" role="img" aria-label="Fotografía de fachada ornamentada virada a violeta" style="left:0;top:279px;width:108px;height:315px"></div>
  <div class="photo photo--facade" role="img" aria-label="Fotografía de balcones de edificio en blanco y negro" style="left:108px;top:500px;width:130px;height:94px"></div>
  <div class="illustration" role="img" aria-label="Ilustración de un halcón sosteniendo en el pico a una mujer, sobre fondo lavanda" style="left:108px;top:279px;width:312px;height:221px"></div>

  <div class="title-bar">LA NOCHE INMENSA</div>
  <div class="title-joint">DE</div>
  <div class="title-vertical">LOS PUERTOS</div>
  <div class="author author--first">MARISOL</div>
  <div class="author author--last">FUENTEVILLA</div>
</section>

<section class="cover cover--back" aria-label="Contracubierta">
  <div class="photo photo--sky" role="img" aria-label="Fotografía de cielo con nubes virada a rosa" style="left:0;top:0;width:108px;height:400px"></div>
  <div class="photo photo--clouds" role="img" aria-label="Fotografía de nubes y torre en blanco y negro" style="left:108px;top:0;width:130px;height:210px"></div>
  <div class="photo photo--facade" role="img" aria-label="Fotografía de fachada y balcón en blanco y negro" style="left:108px;top:210px;width:130px;height:384px"></div>
  <div class="photo photo--violet" role="img" aria-label="Fotografía de fachada ornamentada virada a violeta" style="left:0;top:400px;width:108px;height:194px"></div>

  <div class="title-vertical" aria-hidden="true">DELOSPUERTOS</div>

  <p class="blurb blurb--one">Estos son los versos de una mujer a la que le duele la vida; alguien que vibra en cada experiencia con la intensidad del rayo; que reflexiona los altibajos que le han tocado vivir para sacar enseñanzas que la ayuden a ‘salvar su esencia’.</p>
  <p class="blurb blurb--two">Por eso muchos de sus poemas nos duelen en el alma, porque son gritos de auxilio, espectados desde la desesperanza, llamados en busca de alguien que lleve dentro de sí tantas contradicciones e inquietudes -sexuales, intelectuales, ontológicas- como ella.</p>
  <p class="blurb blurb--three">Marisol Fuentevilla busca explicaciones a través de sus emociones no de su intelecto, porque ha comprendido que “no existe ya el péndulo exacto”, todo fluye y confluye en “ese frenesí eterno de la lucha vida - muerte”. Al leerla ella hace florecer nuestras propias intensidades. Dra. Lucía Aranda</p>
</section>

<section class="spine" aria-label="Lomo">
  <div class="title-bar">LA NOCHE INMENSA</div>
  <div class="spine__title-rest">DELOSPUERTOS</div>
  <div class="spine__author">MARISOL<br>FUENTEVILLA</div>
</section>

<div class="label" style="left:110px;top:650px">FRONT COVER</div>
<div class="label" style="left:655px;top:650px">BACK COVER</div>
<div class="label" style="left:297px;top:791px">SPINE</div>

</body>
</html>
```